**** Web design project for VornaSoft ****

For my ICT company VornaSoft I need a website.

We design, build and host web-applications and we have our own CMS product. In the references part we want to show sample websites (thumbnails) + links.

It should look modern (WEB 2.0), rounded corners.

I want the following menu' s:
- Home
- Services
- References
- News
- About VornaSoft
- Contact

Sample websites:
See attachments
http://www.plumvest.com
http://www.gadomirbureauwerk.nl

Reason: Want to take some time for feedback and improvements.

Reason: I'm waiting for a black background, with shadow and ambient light. You'll make a good chance!

Industry/Entity Type

It Company

Requirements
Must have
• - Fixed width (1024px), should fit on an IPad2
- Language selection English/Dutch
- Twitter/Facebook/LinkedIn/RSS icons
- Footer for Terms of use and Copyrights
- Search box
- 3 (or more) boxes for information i.e. news, blog or advertisements
Nice to have
• - Footer Site Map
- Contrasting background outside borders
- wide image (rotator) (with transperant sentence block)
- Shadow

```html
<!DOCTYPE html>
<html lang="en">
<head>
<meta charset="utf-8">
<title>VornaSoft</title>
<link rel="stylesheet" href="https://fonts.googleapis.com/css2?family=Arimo:ital,wght@0,400;0,700;1,700&family=PT+Sans:ital,wght@0,400;1,400;1,700&family=Lora:ital@1&display=swap">
<style>
:root{
  --ink:#111;
  --text:#222;
  --brand:#5a7f8c;
  --cyan:#18d6ee;
  --cyan-dark:#06a9c6;
  --hero-top:#0bc4d4;
  --hero-bot:#0b2451;
  --navy:#1b2a4e;
  --navy-dark:#0f1a33;
  --page:#f3f3f3;
  --panel:#fff;
  --gold:#f7c24c;
  --ph-hero:#0d63a8;
  --ph-feature:#8a96a8;
}
*{box-sizing:border-box;margin:0;padding:0}
html,body{width:842px;height:1200px;overflow:hidden}
body{position:relative;background:var(--page);font-family:"Arimo",Arial,sans-serif;color:var(--text)}
.abs{position:absolute}
.header{left:0;top:0;width:842px;height:88px;background:linear-gradient(#fff,#eee)}
.logo{left:118px;top:12px;display:flex;align-items:center;gap:8px}
.logo-dot{width:44px;height:44px;border-radius:50%;background:#2a9fd6}
.logo-name{font-size:20px;color:var(--brand)}
.lang-label{left:603px;top:13px;font-size:9.5px;color:var(--ink)}
.lang-select{left:656px;top:9px;width:78px;height:18px;border:1px solid #aaa;border-radius:3px;background:#fff;font-size:9.5px;padding:3px 6px}
.lang-select span{position:absolute;right:3px;top:3px;width:10px;height:10px;border:1px solid #555;font-size:7px;line-height:8px;text-align:center}
.search{left:561px;top:40px;width:174px;height:19px;border-radius:10px;border:1px solid #bbb;background:#fff;box-shadow:inset 0 1px 2px #ccc;font-size:9px;padding:3px 10px}
.search svg{position:absolute;right:6px;top:3px}
.hero{left:0;top:88px;width:842px;height:345px;background:linear-gradient(var(--hero-top) 0%,#087fa4 35%,var(--hero-bot) 100%)}
.hero-art{left:90px;top:180px;width:662px;height:205px;border-radius:6px;background:radial-gradient(ellipse at 50% 55%,#2fa8e8 0%,var(--ph-hero) 45%,rgba(11,36,81,0) 80%)}
.nav{left:98px;top:72px;width:656px;height:32px;border-radius:14px;background:linear-gradient(#5be9f8,var(--cyan) 50%,var(--cyan-dark));box-shadow:0 3px 5px rgba(0,0,0,.35);display:flex;align-items:center;padding-left:27px}
.nav a{font-size:10.5px;font-weight:700;color:var(--ink);text-decoration:none;margin-right:23.5px}
.social{position:absolute;right:10px;top:9px;display:flex;gap:3px}
.social i{width:14px;height:14px;border-radius:50%;background:#102030}
.hero-title{left:0;top:117px;width:842px;text-align:center;font-family:"PT Sans",sans-serif;font-weight:400;font-size:19px;color:#0c2a33}
.hero-text{left:103px;top:145px;width:650px;text-align:center;font-size:10.6px;letter-spacing:-.1px;line-height:14px;color:#051a22}
.dots{left:411px;top:361px;display:flex;gap:2px}
.dots i{width:9px;height:9px;border-radius:50%;background:#0b1a30}
.dots i.on{background:var(--cyan)}
.bottom{left:0;top:1012px;width:842px;height:188px;background:linear-gradient(var(--navy-dark),var(--navy))}
.panel{left:98px;top:385px;width:658px;height:697px;background:var(--panel);border-radius:6px;box-shadow:0 0 10px rgba(0,0,0,.25)}
.tagline{left:113px;top:404px;font-family:"PT Sans",sans-serif;font-style:italic;font-size:11px;letter-spacing:-.25px;color:#444}
.btn-gold{left:530px;top:396px;width:211px;height:26px;border-radius:13px;background:linear-gradient(#fde28a,var(--gold));box-shadow:0 2px 3px rgba(0,0,0,.3);font-size:10px;font-weight:700;font-style:italic;color:#5a4a20;text-align:center;line-height:26px}
.rule{height:1px;background:linear-gradient(90deg,transparent,#ddd,transparent)}
.h2{font-family:"PT Sans",sans-serif;font-style:italic;font-size:16px;font-weight:400;color:var(--ink);letter-spacing:-.3px}
.img{border-radius:4px}
.lead{left:117px;top:587px;width:396px;font-size:9.6px;font-weight:700;line-height:14px;color:var(--ink)}
.body{font-size:9.4px;line-height:14px;color:var(--text)}
.news-title{font-size:9.6px;font-weight:700;line-height:14px;color:var(--ink);width:195px}
.thumb{width:44px;height:44px;border:1px solid #ccc;padding:3px;background:#fff;box-shadow:0 1px 2px #aaa}
.thumb div{width:100%;height:100%;background:#6a6a6a}
.feat-title{font-size:9.6px;font-weight:700;color:var(--ink)}
.more{font-style:italic;font-weight:700;font-size:8px;color:#1b2f60}
.tweet{left:187px;top:1037px;width:410px;font-family:"Lora",serif;font-style:italic;font-size:10.5px;line-height:14px;color:#999}
.tweet em{color:#3a6ea0;font-size:9.5px}
.btn-follow{left:628px;top:1033px;width:106px;height:28px;border-radius:14px;background:linear-gradient(#f4f4f4,#ccc);border:1px solid #9ed;font-family:"Lora",serif;font-style:italic;font-size:12px;color:#777;text-align:center;line-height:26px}
.foot-dot{left:405px;top:1104px;width:36px;height:36px;border-radius:50%;background:#2a9fd6}
.foot-links{left:0;top:1162px;width:842px;text-align:center;font-size:9px;color:#dde}
.copy{left:0;top:1176px;width:842px;text-align:center;font-size:9px;color:#bbc}
</style>
</head>
<body>
<header class="abs header"></header>
<div class="abs logo"><span class="logo-dot"></span><span class="logo-name">VornaSoft</span></div>
<div class="abs lang-label">Languages:</div>
<div class="abs lang-select">English<span>▾</span></div>
<div class="abs search">search<svg width="10" height="10" viewBox="0 0 10 10"><circle cx="4" cy="4" r="3" fill="none" stroke="#111" stroke-width="1.5"/><line x1="6.2" y1="6.2" x2="9.5" y2="9.5" stroke="#111" stroke-width="1.8"/></svg></div>

<section class="abs hero"></section>
<div class="abs hero-art" role="img" aria-label="Slide image: glowing network of people at laptops joined by light lines"></div>
<nav class="abs nav">
  <a>HOME</a><a>SERVICES</a><a>REFERENCES</a><a>NEWS</a><a>ABOUT VornaSoft</a><a>CONTACT US</a>
  <div class="social"><i></i><i></i><i></i><i></i></div>
</nav>
<h1 class="abs hero-title">Welcome to VornaSoft</h1>
<p class="abs hero-text">At vero eos et accusamus et iusto odio dignissimos ducimus qui blanditiis praesentium voluptatum deleniti atque corrupti quos dolores et quas molestias excepturi sint occaecati cupiditate non provident, similique sunt in culpa qui officia deserunt mollitia animi</p>
<div class="abs dots"><i></i><i class="on"></i><i></i></div>

<div class="abs bottom"></div>
<main class="abs panel"></main>

<p class="abs tagline">Lorem ipsum dolor sit amet, consectetur adipisicing elit, sed do eiusmod tempor...</p>
<div class="abs btn-gold">Learn more about our services</div>
<div class="abs rule" style="left:140px;top:436px;width:570px"></div>

<h2 class="abs h2" style="left:115px;top:461px">We are #1 web-application product in the world</h2>
<div class="abs img" role="img" aria-label="Banner image: glowing network nodes and laptops" style="left:116px;top:490px;width:397px;height:86px;background:linear-gradient(90deg,#0a1f5a,#0d4ea8 50%,#0a1f5a)"></div>
<p class="abs lead">At vero eos et accusamus et iusto odio dignissimos ducimus qui blanditiis praesentium voluptatum deleniti atque corrupti quos dolores et quas molestias excepturi sint occaecati cupiditate non provident</p>
<p class="abs body" style="left:117px;top:642px;width:396px">Ssimilique sunt in culpa qui officia deserunt mollitia animi, id est laborum et dolorum fuga. Et harum quidem rerum facilis est et expedita distinctio. Nam libero tempore, cum soluta nobis est eligendi optio cumque nihil impedit quo minus id quod maxime placeat facere possimus, omnis voluptas assumenda est, omnis dolor repellendus. Temporibus autem quibusdam et aut officiis debitis aut rerum necessitatibus saepe eveniet ut et voluptates repudiandae sint et molestiae</p>

<h2 class="abs h2" style="left:543px;top:461px">Latest News</h2>
<p class="abs news-title" style="left:542px;top:489px">Sed ut perspiciatis unde omnis iste natus error sit voluptatem</p>
<div class="abs thumb" style="left:541px;top:524px"><div role="img" aria-label="News thumbnail photo"></div></div>
<p class="abs body" style="left:596px;top:520px;width:145px">Sed ut perspiciatis unde omnis iste natus error sit voluptatem cusantium doloremque laudantium, totam rem aperiam, eaque ipsa</p>
<p class="abs news-title" style="left:542px;top:588px">Sed ut perspiciatis unde omnis iste natus error sit voluptatem</p>
<div class="abs thumb" style="left:541px;top:623px"><div role="img" aria-label="News thumbnail photo"></div></div>
<p class="abs body" style="left:596px;top:619px;width:145px">Sed ut perspiciatis unde omnis iste natus error sit voluptatem cusantium doloremque laudantium, totam rem aperiam, eaque ipsa</p>

<div class="abs rule" style="left:115px;top:732px;width:625px;background:#e6e6e6"></div>
<h2 class="abs h2" style="left:115px;top:745px">Feature Services</h2>

<div class="abs img" role="img" aria-label="Feature photo: business handshake" style="left:112px;top:779px;width:202px;height:86px;background:linear-gradient(#5a6478,#8a92a2)"></div>
<div class="abs img" role="img" aria-label="Feature photo: keyboard key with mail symbol" style="left:324px;top:779px;width:202px;height:86px;background:linear-gradient(#9aa096,#b4b8ae)"></div>
<div class="abs img" role="img" aria-label="Feature photo: laptop outdoors" style="left:537px;top:779px;width:202px;height:86px;background:linear-gradient(#8aa6b4,#8e9e88)"></div>

<h3 class="abs feat-title" style="left:114px;top:880px">At vero eos et accusamus</h3>
<p class="abs body" style="left:114px;top:897px;width:204px">Et iusto odio dignissimos ducimus qui blanditiis praesentium voluptatum deleniti atque corrupti quos dolores et quas molestias excepturi sint occaecati cupiditate non provident, similique sunt in culpa qui officia deserunt mollitia animi, id est laborum <span class="more">Read More</span></p>
<h3 class="abs feat-title" style="left:325px;top:880px">At vero eos et accusamus</h3>
<p class="abs body" style="left:325px;top:897px;width:204px">Et iusto odio dignissimos ducimus qui blanditiis praesentium voluptatum deleniti atque corrupti quos dolores et quas molestias excepturi sint occaecati cupiditate non provident, similique sunt in culpa qui officia deserunt mollitia animi, id est laborum <span class="more">Read More</span></p>
<h3 class="abs feat-title" style="left:540px;top:880px">At vero eos et accusamus</h3>
<p class="abs body" style="left:540px;top:897px;width:204px">Et iusto odio dignissimos ducimus qui blanditiis praesentium voluptatum deleniti atque corrupti quos dolores et quas molestias excepturi sint occaecati cupiditate non provident, similique sunt in culpa qui officia deserunt mollitia animi, id est laborum <span class="more">Read More</span></p>

<div class="abs rule" style="left:160px;top:1012px;width:540px"></div>
<p class="abs tweet">A quick thank you to all of our awesome clients and families that support the Lumora Hosting family and let us do what we love to do! # ~ <em>few moment ago</em></p>
<div class="abs btn-follow">Folow Us</div>

<div class="abs foot-dot"></div>
<div class="abs foot-links">Term of Use &nbsp;|&nbsp;&nbsp; Privacy Policy</div>
<div class="abs copy">Copyright © 2012 - VornaSoft, LLC. - All Rights Reserved</div>
</body>
</html>
```